Thimble Nook web site

I have been running an online business for 6 years.
www.thimblenook.com.au I specialise in ribbons, buttons and unique craft materials. I sell online to individuals and shops with seperate retail and wholesale sites. The web page I'd like redesigned is my retail site.

It needs a clean, fresh look. I've recently had a new logo designed (thanks pixel harbour!) and want the web site to incorporate the new design and colour scheme of black and white. (new logo attached as a file)

I no longer want the page with the large image www.thimblenook.com.au I want to have the first page as the retail shop homepage.
http://www.thimblenook.com.au/index.php so this page needs to have all the links

I want to the look to be fresh, modern and clear. It needs to be quick to load.

Notes from my IT guru: They need to know that the following tend to remain static with just the content section changing on each page; Header Left column (but different in the cart) right column (if required) footer
Updates

Thanks for your designs. 1/3 of my users use mobile devices so please take that into consideration. I would like the logo to be incorporated into the design and be a prominent feature (most have just used it as a tiny image in the top left corner. I would like it to be larger and more prominent.  thanks                                   

Thanks to all the designers who have submitted. Can you please add  'Boutique craft supplies' near the logo. That is my tag line. Thanks

Target Market(s)

Crafty females of all ages

Industry/Entity Type

Business

Requirements
Must have
• links to;
blog
gallery
chatterloop
snapboardly
wholesale
space for an image which I change approx every 2 weeks
about Thimble Nook
contact
privacy policy
terms and conditions
newsletter sign up
shipping info
product search
Nice to have
• I am not sure if I want product images on the homepage? I have attached a few images.
Should not have
• not too much colour - I hate the green border I have now

```html
<!DOCTYPE html>
<html lang="en">
<head>
<meta charset="utf-8">
<title>Thimble Nook – Boutique craft supplies</title>
<link rel="stylesheet" href="https://fonts.googleapis.com/css2?family=Arimo:wght@400;700&display=swap">
<style>
:root{
  --ink:#111;
  --text:#333;
  --muted:#666;
  --line:#ddd;
  --soft:#f2f2f2;
  --footer:#e6e6e6;
  --page:#fff;
}
*{box-sizing:border-box;margin:0;padding:0}
html,body{width:864px;height:1200px;overflow:hidden}
body{font-family:"Arimo",Arial,sans-serif;color:var(--text);
  background:linear-gradient(135deg,#b9b9b9,#8d8d8d 50%,#b3b3b3)}
.abs{position:absolute}
.page{position:absolute;left:72px;top:0;width:722px;height:1172px;background:var(--page)}
.topbar{left:0;top:0;width:722px;height:5px;background:var(--ink)}
.brand{left:18px;top:28px;width:130px;font-size:27px;line-height:30px;color:var(--ink);font-weight:400;text-align:center}
.account-links{left:490px;top:19px;font-size:9px;color:#444}
.account-links span{margin:0 4px;color:#888}
.cart{left:630px;top:0;width:72px;height:44px;background:var(--ink);color:#fff;font-size:10px;text-align:right;padding:6px 8px 0 0;line-height:13px;
  clip-path:polygon(0 0,100% 0,100% 88%,50% 100%,0 88%)}
.cart svg{position:absolute;left:6px;top:6px}
.phone{left:585px;top:67px;font-size:14px;color:var(--ink);letter-spacing:.5px;display:flex;align-items:center;gap:6px}
.nav{left:0;top:110px;width:722px;height:32px;border-top:1px solid var(--line);border-bottom:3px solid var(--ink);background:linear-gradient(#fff,#f4f4f4)}
.nav ul{list-style:none;display:flex;position:absolute;left:18px;top:7px}
.nav li{font-size:13px;color:#555;padding:0 24px;border-left:1px solid #ccc;line-height:16px}
.nav li:first-child{padding-left:0;border-left:0;color:var(--ink)}
.search{left:550px;top:4px;width:152px;height:21px;border:1px solid var(--line);background:#fff;font-size:9px;color:#aaa;padding:5px 7px}
.search svg{position:absolute;right:4px;top:3px}
.categories{left:18px;top:162px;width:174px;height:238px;border:1px solid var(--line);background:#fafafa}
.categories h2{height:28px;background:linear-gradient(#333,#000);color:#fff;font-weight:400;font-size:15px;padding:6px 11px}
.categories ul{list-style:none;padding:3px 12px}
.categories li{font-size:9px;color:#333;height:26px;line-height:26px;border-bottom:1px solid #e4e4e4;padding-left:16px;position:relative}
.categories li:last-child{border-bottom:0}
.categories li::before{content:"➜";position:absolute;left:0;font-size:8px;color:#222}
.hero{left:212px;top:162px;width:490px;height:238px;border:1px solid var(--line);
  background:linear-gradient(160deg,#e7e6ea 0%,#c9b7e4 40%,#e8c6d6 60%,#dfe7b4 80%,#cfcfcf 100%)}
.hero-caption{position:absolute;left:0;bottom:0;width:100%;height:34px;background:rgba(110,110,110,.75);color:#fff;font-size:19px;padding:5px 9px;letter-spacing:.3px}
.arrow{width:18px;height:34px;background:#eee;border:1px solid #ccc}
.arrow svg{margin:11px 4px}
.card{width:139px;height:140px}
.card svg.frame{position:absolute;left:0;top:0}
.card .thumb{position:absolute;left:25px;top:12px;width:89px;height:68px;border-radius:6px}
.card h3{position:absolute;top:87px;width:100%;text-align:center;font-size:10.5px;font-weight:400;color:var(--ink)}
.card .btn{position:absolute;left:44px;top:108px;width:51px;height:21px;background:linear-gradient(#444,#000);color:#fff;border-radius:3px;font-size:9px;text-align:center;line-height:21px}
.t-spool{background:linear-gradient(#d7d23a 0 12%,#6aaed8 12% 88%,#d7d23a 88%)}
.t-buttons{background:radial-gradient(circle,#f4f4f4 40%,#cfcfcf 100%)}
.t-flowers{background:radial-gradient(circle,#e53a3a 30%,#b51e1e 80%,#fff 81%)}
.t-tape{background:linear-gradient(90deg,#8fd0e6,#5cb6d6)}
.info{left:23px;top:774px;width:677px;height:182px}
.info svg.frame{position:absolute;left:0;top:0}
.col{position:absolute;top:10px;width:180px;height:164px}
.col h2{font-size:15px;font-weight:400;color:var(--ink);margin-bottom:6px;line-height:18px}
.col p{font-size:8.6px;line-height:11.8px;color:#333}
.col a{font-size:9.5px;line-height:12px;color:var(--ink);font-weight:700;text-decoration:underline;position:absolute;left:0;top:150px}
.divider{position:absolute;top:12px;height:160px;border-left:1px dotted #999}
.post{display:flex;gap:10px;align-items:flex-start;margin-bottom:4px}
.post h3{font-size:11px;font-weight:700;color:var(--ink);margin-top:2px}
.post-text{margin-bottom:8px}
.post-sep{border-top:1px dotted #999;width:172px;margin:2px 0 10px}
.quote{color:#bbb;font-size:14px;line-height:8px}
.byline{position:absolute;left:0;top:150px;font-size:9.5px;line-height:12px;color:#333}
.byline b{color:var(--ink)}
.social-bar{left:0;top:986px;width:722px;height:38px;border-top:4px solid var(--soft);background:#fff}
.follow{position:absolute;left:18px;top:8px;font-size:11px;color:var(--ink);display:flex;align-items:center;gap:9px}
.dot{width:20px;height:20px;border-radius:50%;background:#f3f3f3;border:1px solid #ddd;display:inline-block}
.newsletter{position:absolute;left:280px;top:6px;display:flex;align-items:center;gap:10px;font-size:11px;color:var(--ink)}
.newsletter .field{width:244px;height:20px;border:1px solid #ccc;font-size:7.5px;color:#777;padding:5px 6px}
.newsletter .signup{width:50px;height:20px;background:var(--ink);color:#fff;font-size:10px;text-align:center;line-height:20px;border-radius:2px}
.footer{left:0;top:1024px;width:722px;height:124px;background:var(--footer);border-top:1px solid #ccc}
.fcol{position:absolute;top:16px}
.fcol h4{font-size:11px;font-weight:400;color:var(--ink);margin-bottom:7px}
.fcol li{list-style:none;font-size:8.5px;line-height:15.6px;color:#555}
.fcol p{font-size:8.5px;line-height:12px;color:#555;width:170px}
.contact-row{display:flex;align-items:center;gap:6px;font-size:8.5px;color:#555;margin-top:8px}
.cards{display:flex;gap:2px;margin-top:6px}
.paycard{width:36px;height:24px;border:1px solid #bbb;background:#fff;font-size:6.5px;color:var(--ink);text-align:center;line-height:22px;border-radius:2px}
.seal{width:96px;height:24px;margin-top:8px;background:#fff;border:1px solid #bbb;border-radius:2px}
.legal{left:0;top:1148px;width:722px;height:24px;background:linear-gradient(#d6d6d6,#c9c9c9);font-size:8px;color:var(--ink);padding:7px 18px;display:flex;justify-content:space-between}
</style>
</head>
<body>
<div class="page">
  <div class="abs topbar"></div>

  <header>
    <div class="abs brand">Thimble Nook</div>
    <div class="abs account-links">My Account<span>|</span>Checkout<span>|</span>Log In</div>
    <div class="abs cart">
      <svg width="16" height="13" viewBox="0 0 16 13"><path d="M0 1h3l2 7h8l2-5H4" fill="none" stroke="#fff" stroke-width="1.3"/><circle cx="6" cy="11" r="1.3" fill="#fff"/><circle cx="12" cy="11" r="1.3" fill="#fff"/></svg>
      My Cart<br>(0) Items
    </div>
    <div class="abs phone">
      <svg width="16" height="16" viewBox="0 0 16 16"><circle cx="8" cy="8" r="7.3" fill="none" stroke="#111" stroke-width="1.2"/><path d="M5.5 4.5l1.5 1.5-1 1c.6 1.3 1.6 2.3 2.9 2.9l1-1 1.5 1.5-1.2 1.2C7.6 11.3 4.7 8.4 4.3 5.7z" fill="#111"/></svg>
      (555) 218 4400
    </div>
    <nav class="abs nav">
      <ul><li>Home</li><li>Shop</li><li>Wholesale</li><li>Gallery</li><li>Blog</li><li>Contact</li></ul>
      <div class="abs search">Search
        <svg width="13" height="13" viewBox="0 0 13 13"><circle cx="5" cy="5" r="3.8" fill="none" stroke="#999" stroke-width="1.5"/><path d="M8 8l4 4" stroke="#999" stroke-width="1.8"/></svg>
      </div>
    </nav>
  </header>

  <aside class="abs categories">
    <h2>Our Categories</h2>
    <ul>
      <li>Lorem ipsum dolor sit amet</li><li>Lorem ipsum dolor sit amet</li><li>Lorem ipsum dolor sit amet</li><li>Lorem ipsum dolor sit amet</li>
      <li>Lorem ipsum dolor sit amet</li><li>Lorem ipsum dolor sit amet</li><li>Lorem ipsum dolor sit amet</li><li>Lorem ipsum dolor sit amet</li>
    </ul>
  </aside>

  <section class="abs hero" role="img" aria-label="Photo of coiled pastel gingham ribbons in lilac, pink, yellow and blue">
    <div class="hero-caption">I specialise in ribbons,and unique craft materials</div>
  </section>
  <div class="abs arrow" style="left:207px;top:264px"><svg width="8" height="10" viewBox="0 0 8 10"><path d="M6 1L2 5l4 4" fill="none" stroke="#222" stroke-width="2"/></svg></div>
  <div class="abs arrow" style="left:689px;top:264px"><svg width="8" height="10" viewBox="0 0 8 10"><path d="M2 1l4 4-4 4" fill="none" stroke="#222" stroke-width="2"/></svg></div>

  <main>
    <div class="abs card" style="left:23px;top:426px">
      <svg class="frame" width="139" height="140"><path d="M10 .5h119l9.5 10v119l-9.5 10H10L.5 129.5v-119z" fill="#fff" stroke="#ddd"/></svg>
      <div class="thumb t-spool" role="img" aria-label="Spool of blue ribbon"></div>
      <h3>Lorem ipsum dolor sit</h3><div class="btn">Details</div>
    </div>
    <div class="abs card" style="left:202px;top:426px">
      <svg class="frame" width="139" height="140"><path d="M10 .5h119l9.5 10v119l-9.5 10H10L.5 129.5v-119z" fill="#fff" stroke="#ddd"/></svg>
      <div class="thumb t-buttons" role="img" aria-label="White buttons with black dots"></div>
      <h3>Lorem ipsum dolor sit</h3><div class="btn">Details</div>
    </div>
    <div class="abs card" style="left:380px;top:426px">
      <svg class="frame" width="139" height="140"><path d="M10 .5h119l9.5 10v119l-9.5 10H10L.5 129.5v-119z" fill="#fff" stroke="#ddd"/></svg>
      <div class="thumb t-flowers" role="img" aria-label="Red ribbon flowers"></div>
      <h3>Lorem ipsum dolor sit</h3><div class="btn">Details</div>
    </div>
    <div class="abs card" style="left:559px;top:426px">
      <svg class="frame" width="139" height="140"><path d="M10 .5h119l9.5 10v119l-9.5 10H10L.5 129.5v-119z" fill="#fff" stroke="#ddd"/></svg>
      <div class="thumb t-tape" role="img" aria-label="Rolls of blue patterned tape"></div>
      <h3>Lorem ipsum dolor sit</h3><div class="btn">Details</div>
    </div>
    <div class="abs card" style="left:23px;top:599px">
      <svg class="frame" width="139" height="140"><path d="M10 .5h119l9.5 10v119l-9.5 10H10L.5 129.5v-119z" fill="#fff" stroke="#ddd"/></svg>
      <div class="thumb t-buttons" role="img" aria-label="White buttons with black dots"></div>
      <h3>Lorem ipsum dolor sit</h3><div class="btn">Details</div>
    </div>
    <div class="abs card" style="left:202px;top:599px">
      <svg class="frame" width="139" height="140"><path d="M10 .5h119l9.5 10v119l-9.5 10H10L.5 129.5v-119z" fill="#fff" stroke="#ddd"/></svg>
      <div class="thumb t-spool" role="img" aria-label="Spool of blue ribbon"></div>
      <h3>Lorem ipsum dolor sit</h3><div class="btn">Details</div>
    </div>
    <div class="abs card" style="left:380px;top:599px">
      <svg class="frame" width="139" height="140"><path d="M10 .5h119l9.5 10v119l-9.5 10H10L.5 129.5v-119z" fill="#fff" stroke="#ddd"/></svg>
      <div class="thumb t-tape" role="img" aria-label="Rolls of blue patterned tape"></div>
      <h3>Lorem ipsum dolor sit</h3><div class="btn">Details</div>
    </div>
    <div class="abs card" style="left:559px;top:599px">
      <svg class="frame" width="139" height="140"><path d="M10 .5h119l9.5 10v119l-9.5 10H10L.5 129.5v-119z" fill="#fff" stroke="#ddd"/></svg>
      <div class="thumb t-flowers" role="img" aria-label="Red ribbon flowers"></div>
      <h3>Lorem ipsum dolor sit</h3><div class="btn">Details</div>
    </div>

    <section class="abs info">
      <svg class="frame" width="677" height="182"><path d="M12 .5h653l11.5 12v157l-11.5 12H12L.5 169.5v-157z" fill="#fff" stroke="#ddd"/></svg>
      <div class="col" style="left:14px">
        <h2>About Us</h2>
        <p>Lorem ipsum dolor sit amet, consec tetur adipisicing elit, sed do eiusmod tempor incididunt ut labore et dolore magna aliqua. Ut enim ad minim veniam, quis nostrud exercitation ullamco laboris nisi ut aliquip ex ea commodo consequat. Duis aute irure dolor in reprehenderit in voluptate velit esse cillum dolore eu fugiat nulla pariatur. Ut enim ad minim veniam, quis nostrud.</p>
        <a>More Post</a>
      </div>
      <div class="divider" style="left:221px"></div>
      <div class="col" style="left:248px">
        <h2>Our Blog</h2>
        <div class="post"><svg width="22" height="16" viewBox="0 0 22 16"><rect x="1" y="1" width="20" height="14" fill="none" stroke="#111" stroke-width="1.6"/><rect x="4" y="4" width="6" height="5" fill="#111"/><path d="M12 5h6M12 8h6M4 11h14" stroke="#111" stroke-width="1.3"/></svg><h3>Lorem ipsum dolor SIT</h3></div>
        <p class="post-text">Lorem ipsum dolor sit amet, consectetur adipisicing elit, sed do eiusmod tempor</p>
        <div class="post-sep"></div>
        <div class="post"><svg width="22" height="16" viewBox="0 0 22 16"><rect x="1" y="1" width="20" height="14" fill="none" stroke="#111" stroke-width="1.6"/><rect x="4" y="4" width="6" height="5" fill="#111"/><path d="M12 5h6M12 8h6M4 11h14" stroke="#111" stroke-width="1.3"/></svg><h3>Lorem ipsum dolor SIT</h3></div>
        <p class="post-text">Lorem ipsum dolor sit amet, consectetur adipisicing elit, sed do eiusmod tempor</p>
        <a>More Post</a>
      </div>
      <div class="divider" style="left:456px"></div>
      <div class="col" style="left:482px">
        <h2>Testimonial</h2>
        <p><span class="quote">“</span> Lorem ipsum dolor sit amet, consectetur adipisicing elit, sed do eiusmod tempor incididunt ut labore et dolore magna aliqua. Ut enim ad minim veniam, quis nostrud exercitation ullamco laboris nisi ut aliquip ex ea commodo consequat. Duis aute irure dolor in reprehenderit in voluptate velit esse cillum dolore eu fugiat nulla pariatur. Duis aute irure dolo. <span class="quote">”</span></p>
        <div class="byline"><b>By:</b> Lorem Ipsum</div>
      </div>
    </section>
  </main>

  <div class="abs social-bar">
    <div class="follow">Follow Us
      <span class="dot" role="img" aria-label="chatterloop"></span>
      <span class="dot" role="img" aria-label="Chirpwire"></span>
      <span class="dot" role="img" aria-label="snapboardly"></span>
    </div>
    <div class="newsletter">Sign Up for Newsletter
      <div class="field">Enter your Email Address</div>
      <div class="signup">Signup</div>
    </div>
  </div>

  <footer class="abs footer">
    <div class="fcol" style="left:18px"><h4>Quick Links</h4>
      <ul><li>Home</li><li>Shop</li><li>Wholesale</li><li>Gallery</li><li>Blog</li></ul></div>
    <div class="fcol" style="left:139px"><h4>Customer Service</h4>
      <ul><li>My Account</li><li>Order Tracking</li><li>Shipping / Returns</li><li>Privacy Policy</li><li>Tell A Friend</li></ul></div>
    <div class="fcol" style="left:294px"><h4>Contact Details</h4>
      <p>Lorem ipsum dolor sit amet, consectetur adipisicing elit, sed do eiusmod temp.</p>
      <div class="contact-row"><svg width="9" height="9" viewBox="0 0 9 9"><path d="M1 1l2 0 1 2-1 1c.5 1 1 1.5 2 2l1-1 2 1v2C5 8 1 4 1 1z" fill="#222"/></svg>(000) 000 - 0000</div>
      <div class="contact-row"><svg width="9" height="7" viewBox="0 0 9 7"><rect width="9" height="7" fill="#222"/><path d="M0 0l4.5 4L9 0" fill="none" stroke="#e6e6e6"/></svg>info@loremipsum.com</div>
    </div>
    <div class="fcol" style="left:509px"><h4>Payment Option</h4>
      <div class="cards"><div class="paycard">PayNest</div><div class="paycard">Veyra</div><div class="paycard">OrbCard</div><div class="paycard">Findly</div><div class="paycard">Crestpay</div></div>
      <div class="seal" role="img" aria-label="Site security seal"></div>
    </div>
  </footer>

  <div class="abs legal"><span>Terms &amp; Conditions</span><span>Copyright © 2013</span></div>
</div>
</body>
</html>
```